Vorel constructions

We are predominantly a residential home builder based in Melbourne, Victoria Australia. We construct houses, apartments, townhouses, multi-unit developments.

The name of the company is "Vorel Constructions"
My company believes in building unique construction projects mainly residential homes. The target customers are upmarket Melbourne residents/investors.

I want the brand name "Vorel" to be part of the logo. There's no need to put the word construction in the logo at this stage.

I would also like some ideas for a slogan e.g. "Just build it." or "We build quality homes." But I would like something unique and different for a slogan not the same old cliche.

vorelconstructions.example.com.au
e: tmelo@vorelconstructions.example.com.au
M: 0417305862
Address: 8/3 Fenwick Lane Clayton VIC 3168

Director:Mr Dinesh Malarkodiyan

```html
<!DOCTYPE html>
<html lang="en">
<head>
<meta charset="utf-8">
<title>Vorel Constructions – Business Cards</title>
<link href="https://fonts.googleapis.com/css2?family=Didact+Gothic&family=Arimo:wght@400&display=swap" rel="stylesheet">
<style>
  :root {
    --backdrop: #3b3b3d;
    --navy: #1e1958;
    --navy-deep: #17124a;
    --silver: #c8c8c9;
    --cyan: #2aaee3;
    --white: #ffffff;
  }
  * { margin: 0; padding: 0; box-sizing: border-box; }
  html, body {
    width: 1200px; height: 720px; overflow: hidden;
    background: var(--backdrop);
  }
  .canvas { position: relative; width: 1200px; height: 720px; }

  .card {
    position: absolute;
    width: 520px; height: 300px;
    border-radius: 26px;
    overflow: hidden;
    box-shadow: 0 10px 28px rgba(0,0,0,0.45);
  }

  /* Front */
  .card-front {
    left: 70px; top: 70px;
    background: var(--navy);
    font-family: "Didact Gothic", sans-serif;
    color: var(--white);
  }
  .card-front .brand {
    position: absolute; left: 190px; top: 92px;
    font-size: 62px; letter-spacing: 2px;
    color: var(--cyan);
    line-height: 1;
  }
  .card-front .tagline {
    position: absolute; left: 0; right: 0; top: 218px;
    text-align: center;
    font-size: 19px;
  }

  /* Back */
  .card-back {
    left: 610px; top: 350px;
    background: var(--navy-deep);
    font-family: "Arimo", sans-serif;
    color: var(--white);
  }
  .card-back .top-band {
    position: absolute; left: 0; top: 0; right: 0; height: 150px;
    background: var(--silver);
  }
  .card-back .brand {
    position: absolute; left: 66px; top: 70px;
    font-family: "Didact Gothic", sans-serif;
    font-size: 42px; letter-spacing: 1px;
    color: var(--cyan); line-height: 1;
  }
  .contact-list {
    position: absolute; left: 150px; top: 168px;
    list-style: none;
  }
  .contact-item {
    display: flex; align-items: center; gap: 16px;
    margin-bottom: 12px;
    font-size: 14px; line-height: 1.25;
  }
  .contact-item svg { flex: none; width: 24px; height: 22px; }
  .contact-item.phone { font-size: 17px; }
</style>
</head>
<body>
<main class="canvas">
  <section class="card card-front" aria-label="Business card front">
    <div class="brand">Vorel</div>
    <p class="tagline">Qulity House For an Qulity Life</p>
  </section>

  <section class="card card-back" aria-label="Business card back">
    <div class="top-band"></div>
    <div class="brand">Vorel</div>
    <ul class="contact-list">
      <li class="contact-item">
        <svg viewBox="0 0 24 22" aria-hidden="true"><path d="M2 11 L12 2 L22 11 M5 9 V20 H19 V9 M10 20 V14 H14 V20" fill="none" stroke="#fff" stroke-width="1.6"/></svg>
        <span>8/3 Fenwick Lane Clayton VIC 3168</span>
      </li>
      <li class="contact-item">
        <svg viewBox="0 0 24 22" aria-hidden="true"><rect x="2" y="5" width="20" height="13" fill="none" stroke="#fff" stroke-width="1.6"/><path d="M2 5 L12 13 L22 5" fill="none" stroke="#fff" stroke-width="1.6"/></svg>
        <span>tmelo@vorelconstructions.example.com.au<br>vorelconstructions.example.com.au</span>
      </li>
      <li class="contact-item phone">
        <svg viewBox="0 0 24 22" aria-hidden="true"><rect x="3" y="1" width="18" height="20" rx="3" fill="#fff"/><path d="M9 5 C7 7 8 12 11 15 C13 17 15 18 16 17 L15 14.5 L13.5 15 C12 14 10.5 12 10 10 L11.2 9 L10 5 Z" fill="#17124a"/></svg>
        <span>0417305862</span>
      </li>
    </ul>
  </section>
</main>
</body>
</html>
```